Hispanic Financial Counseling and Advocate Firm seeks business card design

Looking for a clean, professional business card design. This is a firm that specializes in providing financial education, coaching, and planning to the Hispanic community. The name of the company is Valendo, which means to prosper. We need a design that is clean, professional, and invokes trust, professionalism, but also welcoming. Our logo is a plant growing from a hand to give the messaging of of being in control of growing your financial future and security. Its part of a larger organization names Cresta Financial Group, who's logo is a tree with multi colored branches. We have the back of the card designed so we just need the front designed. the back is blue, so front needs to be a different background color, not blue.

Target Market(s)

Hispanic Community looking to better their future

Industry/Entity Type

financial services

Contact Information for Business Card

contact info: Ernesto Villalba Jr, 951-555-4613, info@crestafinancialgroup.example. Crestafinancialgroup.example. tag line: Para un futuro mas seguro!

Requirements
Must have
• basics: logo, contact info.
Nice to have
• possibly incorporate the tree logo provided somehow
Should not have
• should not look like the back, needs to be different from the back provided.

```html
<!DOCTYPE html>
<html lang="es">
<head>
<meta charset="utf-8">
<title>Valendo – Tarjeta de presentación</title>
<link rel="stylesheet" href="https://fonts.googleapis.com/css2?family=Montserrat:wght@400;500;700;800&display=swap">
<style>
  :root {
    --bg: #e9eaec;
    --navy: #0d2c45;
    --slate: #4a5876;
    --green: #5fa832;
    --white: #ffffff;
    --leaf-green: #7cc142;
    --leaf-blue: #2ea3dc;
    --leaf-red: #e8413c;
    --leaf-purple: #9a7cc4;
    --leaf-yellow: #f5b918;
  }
  * { margin: 0; padding: 0; box-sizing: border-box; }
  html, body {
    width: 1200px; height: 852px; overflow: hidden;
    background: var(--bg);
    font-family: "Montserrat", sans-serif;
  }
  .canvas { position: relative; width: 1200px; height: 852px; }
  .card {
    position: absolute; width: 665px; height: 380px; overflow: hidden;
    box-shadow: 0 10px 30px rgba(0,0,0,.18);
  }

  /* Back of card */
  .card-back { left: 60px; top: 40px; background: var(--navy); color: var(--white); }
  .parent-brand {
    position: absolute; left: 0; right: 0; top: 95px;
    display: flex; align-items: center; justify-content: center; gap: 22px;
  }
  .parent-mark { width: 90px; height: 90px; border-radius: 50%; background: var(--white); opacity: .92; }
  .parent-divider { width: 1px; height: 100px; background: rgba(255,255,255,.7); }
  .parent-name { font-weight: 700; font-size: 44px; line-height: 1; letter-spacing: -1px; }
  .parent-name small { display: block; font-size: 20px; letter-spacing: .5px; margin-top: 6px; }
  .services {
    position: absolute; left: 0; right: 0; top: 235px;
    text-align: center; font-size: 17px; font-weight: 500; line-height: 1.45;
  }
  .service { white-space: nowrap; margin: 0 4px; }
  .service::before {
    content: ""; display: inline-block; width: 9px; height: 12px;
    border-radius: 50% 50% 50% 50% / 60% 60% 40% 40%;
    margin-right: 6px; vertical-align: -1px; background: var(--dot);
  }

  /* Front of card */
  .card-front { left: 475px; top: 432px; background: var(--white); }
  .card-front svg.shapes { position: absolute; inset: 0; }
  .brand {
    position: absolute; right: 34px; top: 52px;
    display: flex; align-items: center; gap: 10px;
  }
  .brand-mark { width: 26px; height: 26px; border-radius: 50%; background: var(--green); }
  .brand-name { color: var(--green); font-weight: 700; font-size: 34px; letter-spacing: -.5px; }
  .tagline {
    position: absolute; left: 40px; top: 108px;
    color: var(--green); font-weight: 800; font-size: 30px; line-height: 1.12; letter-spacing: 1.5px;
  }
  .contact { position: absolute; left: 40px; top: 238px; color: var(--white); }
  .person-name { font-weight: 800; font-size: 22px; letter-spacing: 1.5px; }
  .person-title { font-size: 14px; font-weight: 400; margin-top: 2px; letter-spacing: .5px; }
  .rule { width: 32px; height: 2px; background: var(--white); margin: 12px 0 10px; }
  .contact-list { list-style: none; font-size: 14px; line-height: 1.55; letter-spacing: .3px; }
  .contact-list li { display: flex; align-items: center; gap: 8px; }
  .contact-list svg { width: 12px; height: 12px; flex: none; }
</style>
</head>
<body>
<main class="canvas">

  <section class="card card-back" aria-label="Reverso de la tarjeta">
    <div class="parent-brand">
      <span class="parent-mark"></span>
      <span class="parent-divider"></span>
      <div class="parent-name">Cresta<small>Financial Group Inc</small></div>
    </div>
    <p class="services">
      <span class="service" style="--dot: var(--leaf-green)">Inmigración</span>
      <span class="service" style="--dot: var(--leaf-blue)">Planificacion Financiera</span><br>
      <span class="service" style="--dot: var(--leaf-red)">Seguros</span>
      <span class="service" style="--dot: var(--leaf-purple)">Impuestos</span>
      <span class="service" style="--dot: var(--leaf-red)">Y mas</span><br>
      <span class="service" style="--dot: var(--leaf-yellow)">Preparación de documentos</span>
    </p>
  </section>

  <section class="card card-front" aria-label="Frente de la tarjeta">
    <svg class="shapes" viewBox="0 0 665 380" width="665" height="380" aria-hidden="true">
      <path fill="var(--slate)" d="M0,232 H300 C352,232 380,186 440,180 C520,172 590,205 665,275 V380 H0 Z"/>
      <path fill="var(--green)" d="M395,132 C430,182 480,158 545,166 C610,176 650,228 665,252 V300 C632,238 592,200 530,194 C470,190 428,188 395,132 Z"/>
    </svg>

    <div class="brand">
      <span class="brand-mark"></span>
      <span class="brand-name">Valendo</span>
    </div>

    <h2 class="tagline">PARA UN FUTURO<br>MAS SEGURO</h2>

    <div class="contact">
      <p class="person-name">ERNESTO VILLALBA JR.</p>
      <p class="person-title">Managing Director</p>
      <div class="rule"></div>
      <ul class="contact-list">
        <li>
          <svg viewBox="0 0 24 24"><path fill="#fff" d="M6.6 10.8a15 15 0 0 0 6.6 6.6l2.2-2.2a1 1 0 0 1 1-.25 11.4 11.4 0 0 0 3.6.57 1 1 0 0 1 1 1V20a1 1 0 0 1-1 1A17 17 0 0 1 3 4a1 1 0 0 1 1-1h3.5a1 1 0 0 1 1 1c0 1.25.2 2.45.57 3.57a1 1 0 0 1-.25 1z"/></svg>
          951-555-4613
        </li>
        <li>
          <svg viewBox="0 0 24 24"><rect x="2" y="5" width="20" height="14" rx="1.5" fill="none" stroke="#fff" stroke-width="2"/><path d="M3 6l9 7 9-7" fill="none" stroke="#fff" stroke-width="2"/></svg>
          info@crestafinancialgroup.example
        </li>
        <li>
          <svg viewBox="0 0 24 24"><circle cx="12" cy="12" r="10" fill="none" stroke="#fff" stroke-width="2"/><path d="M2 12h20M12 2c3 3 3 17 0 20M12 2c-3 3-3 17 0 20" fill="none" stroke="#fff" stroke-width="1.6"/></svg>
          www.crestafinancialgroup.example
        </li>
      </ul>
    </div>
  </section>

</main>
</body>
</html>
```